Motorized Shades, Lighting, Audio Video Control systems needs a website

We need a website similar to Varnell.com which describes our main product solutions (Motorized Shades Fabrication) lighting control and automation systems to create a convenient innovative environment with advance technology, colorful design that can provide comfort and saves on energy.
Updates

Hi Please see Sample adaptation image we need to have the site as per this website: http://www.fenwickop.com/Works/index

Target Market(s)

Mid to high end residential, Commercial building, Offices, Architects

Industry/Entity Type

Environment

Font styles to use
Sans Serif

Colors
0355a3
9bcb3c
fbed24
fbf289
34a7d8
f68e4e
f37122

Requirements
Must have
• some animated slides /banners, possible virtual control of shade and lights animated
Nice to have
• we need website like http://www.fenwickop.com/Works/index with content and colors adapted to our identity (see attached adaptation image)

sample websites to extract from :
Varnell.com
qmbhold.com
morvi.it
pellawin.com

```html
<!DOCTYPE html>
<html lang="en">
<head>
<meta charset="utf-8">
<title>Lumaveil — Motorized Shades, Lighting, Audio Video Control</title>
<link rel="stylesheet" href="https://fonts.googleapis.com/css2?family=Montserrat:wght@300;400;500;600;700&display=swap">
<style>
  :root {
    --page-bg: #ededed;
    --panel-bg: #ffffff;
    --ink: #333333;
    --ink-soft: #555555;
    --ink-nav: #555555;
    --green: #9bcb3c;
    --green-deep: #6fb62e;
    --yellow: #fbed24;
    --yellow-light: #fbf289;
    --blue: #0355a3;
    --blue-deep: #003a86;
    --orange: #f37122;
    --orange-light: #f68e4e;
    --sky: #34a7d8;
  }
  * { box-sizing: border-box; margin: 0; padding: 0; }
  html, body { width: 1060px; height: 1200px; overflow: hidden; }
  body {
    position: relative;
    background: var(--page-bg);
    font-family: "Montserrat", sans-serif;
    color: var(--ink);
  }
  .panel {
    position: absolute; left: 104px; top: 64px;
    width: 848px; height: 1034px;
    background: var(--panel-bg);
  }
  .brand {
    position: absolute; left: 114px; top: 84px;
    display: flex; align-items: center; gap: 8px;
  }
  .brand-mark { width: 22px; height: 36px; background: var(--green); }
  .brand-name {
    font-weight: 700; font-size: 36px; letter-spacing: -1px;
    color: #5f6062; line-height: 1;
  }
  .main-nav a {
    position: absolute; top: 96px;
    font-size: 14px; font-weight: 500; color: var(--ink-nav);
    text-decoration: none;
  }
  .main-nav a.is-active { color: var(--green-deep); }

  .hero {
    position: absolute; left: 114px; top: 142px;
    width: 831px; height: 347px;
    background: linear-gradient(180deg, #e9dcc0 0%, #d9c39a 45%, #6e4a30 80%, #3d2a1e 100%);
  }
  .hero-caption {
    position: absolute; left: 0; bottom: 0; width: 100%; height: 67px;
    background: rgba(200, 196, 190, 0.72);
  }
  .hero-caption p {
    position: absolute; left: 24px; top: 29px;
    font-size: 12.5px; font-weight: 500; color: #111;
  }
  .slider-dots { position: absolute; left: 718px; top: 31px; display: flex; gap: 7px; }
  .slider-dots span { width: 14px; height: 13px; background: #fff; }
  .slider-dots span.is-current { background: var(--green-deep); }

  .solution { position: absolute; top: 513px; width: 266px; text-align: center; }
  .solution-head {
    height: 103px; position: relative; color: #fff;
  }
  .solution-head svg { position: absolute; left: 50%; top: 14px; transform: translateX(-50%); }
  .solution-head h2 {
    position: absolute; left: 0; right: 0; top: 68px;
    font-size: 21px; font-weight: 700; line-height: 1;
  }
  .solution-head h2 span { font-weight: 300; }
  .solution--shades .solution-head { background: linear-gradient(135deg, var(--yellow) 0%, var(--yellow-light) 70%, var(--yellow) 100%); }
  .solution--lighting .solution-head { background: radial-gradient(ellipse at 50% 0%, #1a78cf 0%, var(--blue) 55%, var(--blue-deep) 100%); }
  .solution--av .solution-head { background: linear-gradient(180deg, var(--orange-light) 0%, var(--orange) 100%); }
  .solution p {
    margin-top: 12px;
    font-size: 12.6px; font-weight: 300; line-height: 21px; color: var(--ink-soft);
  }
  .btn-more {
    display: inline-block; margin-top: 14px;
    width: 93px; height: 27px; line-height: 27px;
    font-size: 12px; font-weight: 500; text-decoration: none;
  }
  .solution--shades .btn-more { background: var(--yellow); color: #222; }
  .solution--lighting .btn-more { background: var(--blue-deep); color: #fff; }
  .solution--av .btn-more { background: var(--orange); color: #fff; }

  .section-title {
    position: absolute; top: 792px;
    font-size: 15px; font-weight: 500; color: var(--ink);
  }
  .video {
    position: absolute; left: 114px; top: 833px;
    width: 478px; height: 232px;
    background: linear-gradient(180deg, #cfc2ae 0%, #e6dccb 45%, #a58461 100%);
  }
  .video-actions { position: absolute; right: 10px; top: 11px; display: flex; flex-direction: column; gap: 4px; }
  .video-actions div {
    width: 40px; height: 31px; background: rgba(40, 40, 40, 0.82); border-radius: 3px;
    color: #fff; font-size: 6.5px; font-weight: 700; text-align: center;
    display: flex; flex-direction: column; align-items: center; justify-content: center; gap: 2px;
  }
  .video-play {
    position: absolute; left: 211px; top: 97px; width: 58px; height: 35px;
    background: rgba(35, 35, 35, 0.85); border-radius: 4px;
  }
  .video-bar {
    position: absolute; left: 35px; bottom: 11px; width: 410px; height: 27px;
    background: rgba(30, 30, 30, 0.85); border-radius: 3px;
  }
  .video-track {
    position: absolute; left: 9px; top: 9px; width: 302px; height: 9px;
    border: 1px solid #888; background: #555;
  }
  .video-track i { position: absolute; left: 1px; top: 1px; bottom: 1px; width: 85px; background: var(--sky); }
  .video-track b { position: absolute; left: 86px; top: 1px; bottom: 1px; width: 153px; background: #777; }
  .video-hd { position: absolute; left: 356px; top: 6px; font-size: 12px; font-weight: 700; font-style: italic; color: var(--sky); }

  .testimonial { position: absolute; left: 608px; top: 830px; width: 330px; }
  .avatar {
    position: absolute; left: 113px; top: 0; width: 112px; height: 112px; border-radius: 50%;
    border: 3px solid #c9c9c9; background: radial-gradient(circle at 50% 45%, #d9c8b8 0%, #eeeeee 70%);
  }
  .client-name { position: absolute; left: 0; width: 338px; top: 120px; text-align: center; font-size: 14px; font-weight: 600; }
  .client-company { position: absolute; left: 0; width: 340px; top: 141px; text-align: center; font-size: 12px; font-weight: 300; color: var(--ink-soft); }
  .client-quote {
    position: absolute; left: 6px; top: 175px; width: 330px;
    font-size: 12.4px; font-weight: 300; line-height: 21px; color: var(--ink-soft);
  }

  .footer-nav { position: absolute; left: 104px; top: 1118px; font-size: 12.5px; font-weight: 500; color: var(--ink); }
  .footer-nav a { color: var(--ink); text-decoration: none; }
  .footer-nav .sep { display: inline-block; margin: 0 20px 0 22px; }
  .copyright { position: absolute; left: 104px; top: 1146px; font-size: 12px; font-weight: 500; }
  .social { position: absolute; left: 856px; top: 1133px; display: flex; gap: 11px; }
  .social span { width: 24px; height: 24px; border-radius: 50%; background: #1a1a1a; }
</style>
</head>
<body>
  <div class="panel"></div>

  <header>
    <div class="brand"><span class="brand-mark"></span><span class="brand-name">LUMAVEIL</span></div>
    <nav class="main-nav">
      <a href="#" class="is-active" style="left:378px">Home</a>
      <a href="#" style="left:458px">About Us</a>
      <a href="#" style="left:562px">Services</a>
      <a href="#" style="left:660px">Products</a>
      <a href="#" style="left:762px">Faq’s</a>
      <a href="#" style="left:839px">Contact&nbsp; Us</a>
    </nav>
  </header>

  <section class="hero" role="img" aria-label="Bright living room with motorized window shades, cream sofas and a dining area">
    <div class="hero-caption">
      <p>"Neque porro quisquam est qui dolorem ipsum quia dolor sit amet, consectetur, adipisci velit..."</p>
      <div class="slider-dots"><span class="is-current"></span><span></span><span></span><span></span></div>
    </div>
  </section>

  <article class="solution solution--shades" style="left:114px">
    <div class="solution-head">
      <svg width="34" height="50" viewBox="0 0 34 50"><rect x="2" y="2" width="30" height="46" rx="5" fill="none" stroke="#fff" stroke-width="3"/><rect x="7" y="7" width="20" height="16" fill="#fff"/><circle cx="17" cy="35" r="6" fill="none" stroke="#fff" stroke-width="3"/></svg>
      <h2>Motorized <span>shades</span></h2>
    </div>
    <p>Lorem Ipsum is simply dummy text of the printing and typesetting industry. Lorem Ipsum has been the industry's standard dummy text ever since the 1500s</p>
    <a href="#" class="btn-more">Read More</a>
  </article>

  <article class="solution solution--lighting" style="left:397px">
    <div class="solution-head">
      <svg width="22" height="48" viewBox="0 0 22 48"><g fill="#fff"><rect x="3" y="2" width="16" height="5" rx="2.5"/><rect x="3" y="9" width="16" height="5" rx="2.5"/><rect x="3" y="16" width="16" height="5" rx="2.5"/><rect x="3" y="23" width="16" height="5" rx="2.5"/><path d="M1 30h20l-3 8H4z"/><rect x="6" y="40" width="10" height="3"/><rect x="8" y="44" width="6" height="3"/></g></svg>
      <h2>Lighting</h2>
    </div>
    <p>Lorem Ipsum is simply dummy text of the printing and typesetting industry. Lorem Ipsum has been the industry's standard dummy text ever since the 1500s</p>
    <a href="#" class="btn-more">Read More</a>
  </article>

  <article class="solution solution--av" style="left:679px">
    <div class="solution-head">
      <svg width="38" height="34" viewBox="0 0 38 34" style="top:28px"><path d="M3 8h8l3-5h10l3 5h8v23H3z" fill="none" stroke="#fff" stroke-width="3"/><circle cx="19" cy="19" r="6" fill="none" stroke="#fff" stroke-width="3"/><circle cx="31" cy="13" r="1.8" fill="#fff"/></svg>
      <h2>Audio Video <span>Control</span></h2>
    </div>
    <p>Lorem Ipsum is simply dummy text of the printing and typesetting industry. Lorem Ipsum has been the industry's standard dummy text ever since the 1500s</p>
    <a href="#" class="btn-more">Read More</a>
  </article>

  <h3 class="section-title" style="left:114px">How It Works</h3>
  <div class="video" role="img" aria-label="Video preview of a modern living room with ambient ceiling lighting">
    <div class="video-actions">
      <div><svg width="14" height="12" viewBox="0 0 14 12"><path d="M7 11L1.5 5.5A3 3 0 0 1 7 2a3 3 0 0 1 5.5 3.5z" fill="#fff"/></svg>LIKE</div>
      <div><svg width="13" height="13" viewBox="0 0 13 13"><circle cx="6.5" cy="6.5" r="5.3" fill="none" stroke="#fff" stroke-width="1.5"/><path d="M6.5 3.5v3.2l2 1.4" fill="none" stroke="#fff" stroke-width="1.5"/></svg>LATER</div>
      <div><svg width="13" height="11" viewBox="0 0 13 11"><path d="M2 9l9-7M8 2h3v3" fill="none" stroke="#fff" stroke-width="1.5"/></svg>SHARE</div>
      <div><svg width="16" height="10" viewBox="0 0 16 10"><path d="M5 1L1 5l4 4M11 1l4 4-4 4M9 0L7 10" fill="none" stroke="#fff" stroke-width="1.5"/></svg>EMBED</div>
    </div>
    <div class="video-play"><svg width="58" height="35" viewBox="0 0 58 35"><path d="M24 11v13l11-6.5z" fill="#fff"/></svg></div>
    <div class="video-bar">
      <div class="video-track"><i></i><b></b></div>
      <svg style="position:absolute;left:318px;top:8px" width="30" height="11" viewBox="0 0 30 11"><g fill="#34a7d8"><rect x="0" width="2" height="11"/><rect x="4" width="2" height="11"/><rect x="8" width="2" height="11"/><rect x="12" width="2" height="11"/><rect x="16" width="2" height="11"/><rect x="20" width="2" height="11"/><rect x="24" width="2" height="11"/></g></svg>
      <span class="video-hd">HD</span>
      <svg style="position:absolute;left:384px;top:8px" width="11" height="11" viewBox="0 0 11 11"><path d="M1 1l3 3M10 1L7 4M1 10l3-3M10 10L7 7" stroke="#fff" stroke-width="1.6"/></svg>
    </div>
  </div>

  <h3 class="section-title" style="left:608px">Clients Testimonials</h3>
  <section class="testimonial">
    <div class="avatar" role="img" aria-label="Client portrait"></div>
    <div class="client-name">Daniel Reston</div>
    <div class="client-company">Company Name</div>
    <p class="client-quote">Lorem Ipsum is simply dummy text of the printing and typesetting industry. Lorem Ipsum has been the industry's standard dummy text ever &nbsp;....</p>
  </section>

  <footer>
    <nav class="footer-nav">
      <a href="#">Home</a><span class="sep">|</span><a href="#">About Us</a><span class="sep">|</span><a href="#">Services</a><span class="sep">|</span><a href="#">Products</a><span class="sep">|</span><a href="#">Faq’s</a><span class="sep">|</span><a href="#">Contact&nbsp; Us</a>
    </nav>
    <p class="copyright">© 2014 company name ,all rights reserved</p>
    <div class="social" aria-label="Social links"><span></span><span></span><span></span></div>
  </footer>
</body>
</html>
```